Content Management company needs a new brochure

We help companies transform their content (rework it so it easier to write, read, find, use and share). We work in the topic base structured authoring industry; think information design and the technology needed to create, share and publish exception content. We need a brochure that sells our services while giving us a moderns and progressive identify.

WARNING: our website, www.lumavoreedit.com is being updated. We are moving away from the tree metaphor. Don't use it.

UPDATED....... MAY 13, 2015, 2PM EDT..............

SIZE: All must be US Letter size (8.5 x 11)

This project consists of 3 deliverables:

1. Credit Union Brochure:
I have attached new copy. Ideally this is 1 page; front and back.

2. Before & After example:
Matching the credit union brochure layout, we would like the before and after example. B&A mock-up and source documents attached.

3. What is Lumavore Edit
This is one pager that explains our offering. I would love to see this document in the style of this https://us.pictavane.com/id/52817309

Other styles I like:
http://blog.morvistudio.com/wp-content/uploads/2012/10/Fern-brochure2.jpg
https://www.brevalo.com/pt/quillstack
http://www.deckhollow.net/grenwick/metadata-extraction-and-content-transformation

Target Market(s)

We sell to executive level management at medium to large companies in various sectors. This brochure is focussed on Credit Unions, but we'll need designs for insurance, healthcare, high-tech, etc.

Industry/Entity Type

It Company

Font styles to use
Sans Serif

Colors
0455a3
0792cd
3176b5
85acd3
d2a4cc
b768aa
f68d4c
0292cd
f37122

Requirements
Must have
• Needs to look slick. Not too busy.
Nice to have
• Can't think of anything. We are open to all designs.
Should not have

```html
<!DOCTYPE html>
<html lang="en">
<head>
<meta charset="utf-8">
<title>Credit Unions – Lumavore Edit</title>
<link rel="stylesheet" href="https://fonts.googleapis.com/css2?family=Raleway:ital,wght@0,400;0,500;1,400;1,500;1,700;1,800&display=swap">
<style>
  :root {
    --bg-top: #64bfd6;
    --bg-bottom: #7ccbe0;
    --tint-soft: rgba(255, 255, 255, 0.16);
    --tint-faint: rgba(255, 255, 255, 0.10);
    --badge: #7ab9e6;
    --text: #ffffff;
    --rule: rgba(255, 255, 255, 0.85);
  }
  * { margin: 0; padding: 0; box-sizing: border-box; }
  html, body { width: 914px; height: 1200px; overflow: hidden; }
  body { font-family: "Raleway", Arial, sans-serif; color: var(--text); }

  .brochure {
    position: relative;
    width: 914px;
    height: 1200px;
    overflow: hidden;
    background: linear-gradient(160deg, var(--bg-top) 0%, #6fc6dc 55%, var(--bg-bottom) 100%);
  }

  .texture {
    position: absolute;
    border-radius: 50%;
  }
  .texture--top-left { left: -90px; top: -110px; width: 420px; height: 420px; background: var(--tint-faint); }
  .texture--centre { left: 330px; top: 420px; width: 630px; height: 630px; background: var(--tint-soft); }
  .texture--bottom { left: 340px; top: 1030px; width: 620px; height: 260px; background: var(--tint-faint); border-radius: 0; }

  .badge {
    position: absolute;
    left: 111px; top: 133px;
    width: 222px; height: 222px;
    border-radius: 50%;
    background: var(--badge);
    border: 5px solid #ffffff;
    display: flex; align-items: center; justify-content: center;
    text-align: center;
  }
  .badge__title {
    font-style: italic;
    font-weight: 800;
    font-size: 44px;
    line-height: 1.08;
    letter-spacing: -0.5px;
  }

  .tagline {
    position: absolute;
    left: 392px; top: 202px;
    width: 405px;
    font-style: italic;
    font-size: 21px;
    line-height: 26px;
    text-align: justify;
  }

  .section { position: absolute; }
  .section__heading {
    font-style: italic;
    font-weight: 700;
    font-size: 26px;
    padding-bottom: 4px;
    border-bottom: 1.5px solid var(--rule);
    margin-bottom: 14px;
  }
  .section__body p {
    font-size: 14.2px;
    line-height: 18.4px;
    text-align: justify;
    margin-bottom: 18px;
  }
  .section__list { list-style: none; margin-bottom: 18px; }
  .section__list li {
    font-size: 14.2px;
    line-height: 18.4px;
    text-align: justify;
    padding-left: 10px;
    position: relative;
  }
  .section__list li::before { content: "•"; position: absolute; left: 0; }
  .section__body p.tight { margin-bottom: 0; }

  .section--situation { left: 112px; top: 448px; width: 225px; }
  .section--challenge { left: 392px; top: 368px; width: 405px; }
  .section--solution  { left: 392px; top: 632px; width: 405px; }
</style>
</head>
<body>
<main class="brochure">
  <div class="texture texture--top-left" role="img" aria-label="Soft dotted halftone texture"></div>
  <div class="texture texture--centre" role="img" aria-label="Large translucent circle with dotted halftone texture"></div>
  <div class="texture texture--bottom" role="img" aria-label="Dotted halftone texture along the bottom edge"></div>

  <div class="badge"><h1 class="badge__title">CREDIT<br>UNIONS</h1></div>

  <p class="tagline">Exceeding member expectation through clear, concise, consistent, and effective content</p>

  <section class="section section--situation">
    <h2 class="section__heading">The Situation</h2>
    <div class="section__body">
      <p>Credit union membership has been steadily on the rise as consumers look for alternatives to traditional banking. At the same time a new and evolving consumer is here. Today's credit union member is savvy, informed, equipped with the latest technology, and has higher expectations than ever before.</p>
      <p>As credit unions grow they face challenges around</p>
      <ul class="section__list">
        <li>increasing government regulations around privacy, compliance and accountability</li>
        <li>intensifying competition and complexity from new industry sectors, and</li>
        <li>evolving customer demands for accurate and timely information where and when they want it.</li>
      </ul>
      <p>Credit unions must adjust their business practices to address the impacts of this new reality and the trends driving it. Is your credit unions' content and documentation ready?</p>
    </div>
  </section>

  <section class="section section--challenge">
    <h2 class="section__heading">The Challenge</h2>
    <div class="section__body">
      <p>In this environment, it is critical that policies, procedures, and product information be clear, concise, consistent, easy to find, and easy to use. However, in many organizations this valuable asset is not being strategically leveraged.</p>
      <p>Instead it is written and stored using outdated practices and formats, it resided in multiple locations and versions, and it cannot be easily shared, reused or repurposed. This old way of managing content is inefficient and costly.</p>
    </div>
  </section>

  <section class="section section--solution">
    <h2 class="section__heading">The Solution</h2>
    <div class="section__body">
      <p class="tight">Lumavore Edit™ is a modern way of writing and storing your content so you can manage it like an asset. It leverages XML (eXtensible Markup Language) to make your content usable, flexible, manageable, and portable. Lumavore Edit™ was developed to provide advantages to two main audiences:</p>
      <ul class="section__list">
        <li>The authors who produce content and have to use the software and systems to create, manage and publish it (e.g. content management systems)</li>
        <li>The consumers of content who have to quickly find and understand it (e.g. staff and customers)</li>
      </ul>
    </div>
  </section>
</main>
</body>
</html>
```